Weight gainer supplement design

Looking for a design for a weight gainer /meal replacement supplement. The black plastic tub we will use has 2 spaces for sticker one around the rim approx 2.8cm tall x 30cm wideAnother around the main tub. The main sticker size will be 18cm tall by 70cm this will include the front of the product then wrap around to show the nutritional table.The brand is KTV (Kestrel training vitals) and the product will be called ALPHA MASSThe target ordience is men aged 16-35 its should have a profesional feel to it. The product comes in a black tub, the colores we would like to use are black and blue or red or gold or silver but we are open to suggestions and would like artistic imput. Are logo for KTV is attached but can be changed if the designer prefers.Attached is 1. KTV logo2. Image of similar product that comes in the same tub3 - 5 - images of similar products that we like the design of.The product is 12lbs and will be vanilla flavor. Please ask for more suggestions if needed, I have kept this description short to try and get artistic input.Thanks in advance :)
Updates

Target Market(s)

18-35 males who go to the gym

Industry/Entity Type

Fitness

Colors

Designer to choose colors to be used in the design.

Requirements
Must have
• name bravo bulk, logo KTV
Should not have
• images of people

```html
<!DOCTYPE html>
<html lang="en">
<head>
<meta charset="utf-8">
<title>Bravo Bulk – Tub Label</title>
<link rel="stylesheet" href="https://fonts.googleapis.com/css2?family=Russo+One&family=Roboto+Condensed:wght@400;700&display=swap">
<style>
  :root {
    --page: #e6e6e6;
    --label-black: #0b0b0c;
    --label-edge: #1c1d20;
    --chrome-light: #f4f6f8;
    --chrome-mid: #9aa1a8;
    --chrome-dark: #4a5058;
    --electric-blue: #2f8fe0;
    --sky-blue: #7cc4ff;
    --flame-orange: #f3961c;
    --tag-red: #d3202a;
    --badge-yellow: #f4d21a;
    --tagline-yellow: #f2d73a;
    --cream: #f6efcf;
    --white: #ffffff;
  }
  * { margin: 0; padding: 0; box-sizing: border-box; }
  html, body {
    width: 1200px; height: 916px; overflow: hidden;
    background: var(--page);
  }
  .label {
    position: absolute; left: 100px; top: 78px;
    width: 1000px; height: 760px; overflow: hidden;
    background: linear-gradient(90deg, var(--label-black) 0%, var(--label-edge) 50%, var(--label-black) 100%);
    font-family: "Russo One", sans-serif;
    color: var(--white);
  }
  .top-sheen {
    position: absolute; left: 0; top: 0; width: 560px; height: 150px;
    background: linear-gradient(100deg, rgba(47,143,224,0.55) 0%, rgba(47,143,224,0.15) 45%, transparent 75%);
  }
  .smoke {
    position: absolute; left: 60px; top: 150px; width: 800px; height: 340px;
    background:
      radial-gradient(ellipse at 30% 45%, rgba(60,150,230,0.55) 0%, rgba(30,90,170,0.25) 40%, transparent 70%),
      radial-gradient(ellipse at 75% 55%, rgba(40,120,210,0.35) 0%, transparent 60%);
  }
  .edge-arcs { position: absolute; right: 0; top: 0; width: 200px; height: 760px; }
  .brand {
    position: absolute; left: 40px; top: 32px;
    display: flex; align-items: center; gap: 14px;
  }
  .brand-name { font-size: 58px; line-height: 1; color: var(--white); }
  .brand-dot { width: 14px; height: 14px; border-radius: 50%; background: var(--electric-blue); }
  .value-note {
    position: absolute; left: 200px; top: 66px;
    font-family: "Roboto Condensed", sans-serif; font-size: 15px; color: var(--white);
  }
  .weight-tag {
    position: absolute; left: 150px; top: 92px; width: 150px; height: 46px;
    background: var(--tag-red);
    clip-path: polygon(10% 0, 100% 0, 90% 100%, 0 100%);
    text-align: center; font-size: 34px; line-height: 46px;
  }
  .new-badge {
    position: absolute; left: 770px; top: 50px; width: 96px; height: 96px; border-radius: 50%;
    background: radial-gradient(circle at 40% 35%, #fff48a 0%, var(--badge-yellow) 55%, #b99600 100%);
    color: #1a1a1a; font-family: "Roboto Condensed", sans-serif; font-weight: 700;
    font-size: 30px; line-height: 96px; text-align: center;
  }
  .product-name { position: absolute; left: 0; width: 900px; text-align: center; font-weight: 400; }
  .chrome {
    display: inline-block;
    background: linear-gradient(180deg, var(--chrome-light) 0%, var(--chrome-mid) 45%, var(--chrome-dark) 52%, var(--chrome-light) 100%);
    -webkit-background-clip: text; background-clip: text; color: transparent;
    transform: scaleX(1.15);
  }
  .name-top { top: 160px; font-size: 128px; line-height: 1; }
  .name-bottom { top: 282px; font-size: 190px; line-height: 1; }
  .company {
    position: absolute; left: 0; top: 486px; width: 900px; text-align: center;
    font-size: 38px; letter-spacing: 1px;
    background: linear-gradient(180deg, var(--white) 0%, var(--sky-blue) 100%);
    -webkit-background-clip: text; background-clip: text; color: transparent;
  }
  .tagline {
    position: absolute; left: 0; top: 544px; width: 900px; text-align: center;
    font-family: "Roboto Condensed", sans-serif; font-weight: 700; font-size: 21px;
    color: var(--tagline-yellow);
  }
  .ingredient-note {
    position: absolute; left: 18px; top: 612px;
    font-family: "Roboto Condensed", sans-serif; font-weight: 700; font-size: 16px;
    color: var(--tagline-yellow);
  }
  .accent-stripe {
    position: absolute; left: 0; top: 642px; width: 500px; height: 12px;
    background: var(--badge-yellow);
  }
  .splash {
    position: absolute; left: 700px; top: 580px; width: 200px; height: 90px;
    border-radius: 50% 50% 40% 40%;
    background: radial-gradient(ellipse at 50% 60%, var(--cream) 0%, rgba(246,239,207,0.6) 45%, transparent 72%);
  }
  .flavour {
    position: absolute; left: 690px; top: 664px;
    font-family: "Roboto Condensed", sans-serif; font-weight: 700; font-size: 38px; line-height: 1;
  }
  .flavour-note {
    position: absolute; left: 690px; top: 708px;
    font-family: "Roboto Condensed", sans-serif; font-size: 18px;
  }
</style>
</head>
<body>
  <main class="label">
    <div class="top-sheen"></div>
    <div class="smoke" role="img" aria-label="Blue smoke cloud behind the product name"></div>
    <svg class="edge-arcs" viewBox="0 0 200 760" aria-hidden="true">
      <path d="M60 0 C 150 180, 150 560, 80 760" fill="none" stroke="var(--flame-orange)" stroke-width="10"/>
      <path d="M100 0 C 200 200, 200 560, 130 760 L 200 760 L 200 0 Z" fill="var(--electric-blue)"/>
    </svg>

    <div class="brand"><span class="brand-name">KTV</span><span class="brand-dot"></span></div>
    <div class="value-note">HUGH VALUES</div>
    <div class="weight-tag">12LB</div>
    <div class="new-badge">New</div>

    <h1 class="product-name name-top"><span class="chrome">BRAVO</span></h1>
    <h1 class="product-name name-bottom"><span class="chrome">BULK</span></h1>
    <p class="company">KESTREL TRAINING VITALS</p>
    <p class="tagline">DESIGNED FOR FAST RECOVERY &amp; ULTRA GAIN</p>

    <p class="ingredient-note">GLUTAMINE &amp; MORE</p>
    <div class="accent-stripe"></div>

    <div class="splash" role="img" aria-label="Vanilla milk splash"></div>
    <p class="flavour">Vainllia</p>
    <p class="flavour-note">Natural &amp; Artificial Flavor</p>
  </main>
</body>
</html>
```